Financial Dashboard UI design

We are building a financial dashboard for business management teams, and would like a futuristic and sophisticated design (light and dark themes).

There are a total of 3 screens (attached images: nemo1, nemo2, nemo3).
nemo1 image is comprised of 6 scorecards (attached image: scorecard)
This will also need a design.

So, I'm expecting 4 UI designs in total.

I've added some example UI for inspiration. (sample1 , sample2, sample3, sample4).

Thanks

```html
<!DOCTYPE html>
<html lang="en">
<head>
<meta charset="utf-8">
<title>Variance $ — Financial Dashboard</title>
<link rel="stylesheet" href="https://fonts.googleapis.com/css2?family=Oswald:wght@300;400&display=swap">
<style>
  :root {
    --bg: #17305e;
    --axis: #6f86b8;
    --text: #ffffff;
    --label: #c9d3ea;
    --value: #9bb0dc;
    --col-a-top: #2d5fbf;
    --col-a-bot: #24479a;
    --col-b-top: #234a9c;
    --col-b-bot: #1d3a7c;
    --line-teal: #1de3cf;
    --line-blue: #0aa3f2;
    --line-shadow: #1a2d63;
    --tip: #284a9e;
  }
  html, body {
    margin: 0;
    padding: 0;
    width: 1200px;
    height: 695px;
    overflow: hidden;
    background: var(--bg);
  }
  .dashboard-chart {
    display: block;
    width: 1200px;
    height: 695px;
    font-family: "Oswald", "Arial Narrow", sans-serif;
  }
  .chart-title { fill: var(--text); font-size: 30px; font-weight: 400; text-anchor: middle; }
  .axis-title { fill: var(--text); font-size: 28px; font-weight: 400; text-anchor: middle; }
  .tick-label { fill: var(--text); font-size: 21px; font-weight: 300; text-anchor: end; }
  .category-label { fill: var(--label); font-size: 17px; font-weight: 300; }
  .value-label { fill: var(--value); font-size: 15px; font-weight: 400; }
  .tooltip-text { fill: var(--text); font-size: 14px; font-weight: 400; text-anchor: middle; }
  .axis-line { stroke: var(--axis); stroke-width: 1.5; fill: none; }
  .tick { stroke: var(--axis); stroke-width: 1.5; }
</style>
</head>
<body>
<svg class="dashboard-chart" viewBox="0 0 2520 1460" xmlns="http://www.w3.org/2000/svg" role="img" aria-label="Variance in dollars by budget line">
  <defs>
    <linearGradient id="colA" x1="0" y1="0" x2="0" y2="1">
      <stop offset="0" stop-color="var(--col-a-top)"/>
      <stop offset="1" stop-color="var(--col-a-bot)"/>
    </linearGradient>
    <linearGradient id="colB" x1="0" y1="0" x2="0" y2="1">
      <stop offset="0" stop-color="var(--col-b-top)"/>
      <stop offset="1" stop-color="var(--col-b-bot)"/>
    </linearGradient>
    <linearGradient id="lineGrad" x1="210" y1="0" x2="2040" y2="0" gradientUnits="userSpaceOnUse">
      <stop offset="0" stop-color="var(--line-teal)"/>
      <stop offset="0.76" stop-color="var(--line-teal)"/>
      <stop offset="0.9" stop-color="var(--line-blue)"/>
      <stop offset="1" stop-color="var(--line-blue)"/>
    </linearGradient>
    <clipPath id="areaClip">
      <path d="M210,679 L210,672 C260,670 300,600 375,600 C440,600 480,672 555,672 C620,672 650,455 730,455 C800,455 830,730 905,730 C960,730 1000,245 1075,245 C1140,245 1170,360 1250,365 C1320,370 1340,475 1420,475 C1490,475 1520,603 1600,603 C1660,603 1700,478 1780,478 C1850,478 1880,980 1950,980 C2010,980 2030,720 2042,679 Z"/>
    </clipPath>
  </defs>

  <rect width="2520" height="1460" fill="var(--bg)"/>

  <text class="chart-title" x="1260" y="136">Variance $</text>
  <text class="axis-title" transform="translate(96,679) rotate(-90)">Value</text>

  <g class="y-axis">
    <line class="axis-line" x1="204" y1="215" x2="204" y2="1128"/>
    <line class="tick" x1="194" y1="280" x2="204" y2="280"/>
    <line class="tick" x1="194" y1="467" x2="204" y2="467"/>
    <line class="tick" x1="194" y1="679" x2="204" y2="679"/>
    <line class="tick" x1="194" y1="871" x2="204" y2="871"/>
    <line class="tick" x1="194" y1="1068" x2="204" y2="1068"/>
    <text class="tick-label" x="186" y="287">400k</text>
    <text class="tick-label" x="186" y="474">200k</text>
    <text class="tick-label" x="186" y="688">0</text>
    <text class="tick-label" x="186" y="878">-200k</text>
    <text class="tick-label" x="186" y="1075">-400k</text>
  </g>

  <g class="columns" clip-path="url(#areaClip)">
    <rect x="210" y="200" width="50" height="800" fill="url(#colB)"/>
    <rect x="260" y="200" width="53" height="800" fill="url(#colA)"/>
    <rect x="313" y="200" width="52" height="800" fill="url(#colA)"/>
    <rect x="365" y="200" width="53" height="800" fill="url(#colB)"/>
    <rect x="418" y="200" width="52" height="800" fill="url(#colA)"/>
    <rect x="470" y="200" width="55" height="800" fill="url(#colB)"/>
    <rect x="525" y="200" width="53" height="800" fill="url(#colA)"/>
    <rect x="578" y="200" width="49" height="800" fill="url(#colB)"/>
    <rect x="627" y="200" width="53" height="800" fill="url(#colB)"/>
    <rect x="680" y="200" width="52" height="800" fill="url(#colA)"/>
    <rect x="732" y="200" width="54" height="800" fill="url(#colB)"/>
    <rect x="786" y="200" width="54" height="800" fill="url(#colA)"/>
    <rect x="840" y="200" width="50" height="800" fill="url(#colB)"/>
    <rect x="890" y="200" width="55" height="800" fill="url(#colA)"/>
    <rect x="945" y="200" width="60" height="800" fill="url(#colB)"/>
    <rect x="1005" y="200" width="61" height="800" fill="url(#colA)"/>
    <rect x="1066" y="200" width="61" height="800" fill="url(#colB)"/>
    <rect x="1127" y="200" width="61" height="800" fill="url(#colA)"/>
    <rect x="1188" y="200" width="61" height="800" fill="url(#colB)"/>
    <rect x="1249" y="200" width="61" height="800" fill="url(#colA)"/>
    <rect x="1310" y="200" width="61" height="800" fill="url(#colB)"/>
    <rect x="1371" y="200" width="61" height="800" fill="url(#colA)"/>
    <rect x="1432" y="200" width="61" height="800" fill="url(#colB)"/>
    <rect x="1493" y="200" width="61" height="800" fill="url(#colA)"/>
    <rect x="1554" y="200" width="61" height="800" fill="url(#colB)"/>
    <rect x="1615" y="200" width="61" height="800" fill="url(#colA)"/>
    <rect x="1676" y="200" width="61" height="800" fill="url(#colB)"/>
    <rect x="1737" y="200" width="60" height="800" fill="url(#colA)"/>
    <rect x="1797" y="200" width="61" height="800" fill="url(#colB)"/>
    <rect x="1858" y="200" width="61" height="800" fill="url(#colA)"/>
    <rect x="1919" y="200" width="61" height="800" fill="url(#colB)"/>
    <rect x="1980" y="200" width="62" height="800" fill="url(#colA)"/>
  </g>

  <line class="axis-line" x1="204" y1="679" x2="2476" y2="679"/>
  <line class="axis-line" x1="204" y1="1128" x2="2485" y2="1128"/>

  <g class="variance-line" fill="none" stroke-linecap="round">
    <path stroke="var(--line-shadow)" stroke-width="11" transform="translate(0,6)" d="M210,672 C260,670 300,600 375,600 C440,600 480,672 555,672 C620,672 650,455 730,455 C800,455 830,730 905,730 C960,730 1000,245 1075,245 C1140,245 1170,360 1250,365 C1320,370 1340,475 1420,475 C1490,475 1520,603 1600,603 C1660,603 1700,478 1780,478 C1850,478 1880,980 1950,980 C2010,980 2030,720 2038,679"/>
    <path stroke="url(#lineGrad)" stroke-width="5" d="M210,672 C260,670 300,600 375,600 C440,600 480,672 555,672 C620,672 650,455 730,455 C800,455 830,730 905,730 C960,730 1000,245 1075,245 C1140,245 1170,360 1250,365 C1320,370 1340,475 1420,475 C1490,475 1520,603 1600,603 C1660,603 1700,478 1780,478 C1850,478 1880,980 1950,980 C2010,980 2030,720 2042,679"/>
  </g>

  <g class="value-labels">
    <text class="value-label" transform="translate(240,655) rotate(-90)">1215.0</text>
    <text class="value-label" transform="translate(285,632) rotate(-90)">2568</text>
    <text class="value-label" transform="translate(335,597) rotate(-90)">2568</text>
    <text class="value-label" transform="translate(390,591) rotate(-90)">2568</text>
    <text class="value-label" transform="translate(451,606) rotate(-90)">2568</text>
    <text class="value-label" transform="translate(506,646) rotate(-90)">1025</text>
    <text class="value-label" transform="translate(550,667) rotate(-90)">1025</text>
    <text class="value-label" transform="translate(595,641) rotate(-90)">1025</text>
    <text class="value-label" transform="translate(635,555) rotate(-90)">5987416.30</text>
    <text class="value-label" transform="translate(705,447) rotate(-90)">9654823.30</text>
    <text class="value-label" transform="translate(758,447) rotate(-90)">9654823.30</text>
    <text class="value-label" transform="translate(830,581) rotate(-90)">9654823.30</text>
    <text class="value-label" transform="translate(871,770) rotate(-90)">-98842</text>
    <text class="value-label" transform="translate(927,770) rotate(-90)">-98842</text>
    <text class="value-label" transform="translate(976,510) rotate(-90)">9654823.30</text>
    <text class="value-label" transform="translate(1027,295) rotate(-90)">9654823.30</text>
    <text class="value-label" transform="translate(1106,237) rotate(-90)">9654823.30</text>
    <text class="value-label" transform="translate(1171,287) rotate(-90)">9654823.30</text>
    <text class="value-label" transform="translate(1231,351) rotate(-90)">9654823.30</text>
    <text class="value-label" transform="translate(1299,359) rotate(-90)">9654823.30</text>
    <text class="value-label" transform="translate(1359,412) rotate(-90)">9654823.30</text>
    <text class="value-label" transform="translate(1410,462) rotate(-90)">9654823.30</text>
    <text class="value-label" transform="translate(1477,474) rotate(-90)">9654823.30</text>
    <text class="value-label" transform="translate(1539,545) rotate(-90)">69852</text>
    <text class="value-label" transform="translate(1592,589) rotate(-90)">69852</text>
    <text class="value-label" transform="translate(1641,579) rotate(-90)">69852</text>
    <text class="value-label" transform="translate(1699,514) rotate(-90)">69852</text>
    <text class="value-label" transform="translate(1767,470) rotate(-90)">69852</text>
    <text class="value-label" transform="translate(1844,546) rotate(-90)">69852</text>
    <text class="value-label" transform="translate(1873,863) rotate(-90)">-6969852</text>
    <text class="value-label" transform="translate(2033,895) rotate(-90)">-6969852</text>
  </g>

  <g class="tooltip">
    <path d="M1950,998 L1956,991 L1962,998 Z" fill="var(--tip)"/>
    <rect x="1903" y="998" width="105" height="28" rx="3" fill="var(--tip)"/>
    <text class="tooltip-text" x="1955" y="1017">-965810.02</text>
  </g>

  <g class="category-labels">
    <text class="category-label" transform="translate(228,1142) rotate(90)">Revenue</text>
    <text class="category-label" transform="translate(279,1142) rotate(90)">Foundation Contributions</text>
    <text class="category-label" transform="translate(328,1142) rotate(90)">Individual Contributions</text>
    <text class="category-label" transform="translate(378,1142) rotate(90)">Business Contributions</text>
    <text class="category-label" transform="translate(431,1142) rotate(90)">Grants From National</text>
    <text class="category-label" transform="translate(489,1142) rotate(90)">Other Incomes</text>
    <text class="category-label" transform="translate(544,1142) rotate(90)">Net Assets released from restrion</text>
    <text class="category-label" transform="translate(593,1142) rotate(90)">Total</text>
    <text class="category-label" transform="translate(651,1142) rotate(90)">Salary and related expenses</text>
    <text class="category-label" transform="translate(698,1142) rotate(90)">Salaries and wages</text>
    <text class="category-label" transform="translate(755,1142) rotate(90)">Benifits</text>
    <text class="category-label" transform="translate(810,1142) rotate(90)">Other expenses</text>
    <text class="category-label" transform="translate(857,1142) rotate(90)">Youth activities</text>
    <text class="category-label" transform="translate(912,1142) rotate(90)">Friend activities and transportations</text>
    <text class="category-label" transform="translate(964,1142) rotate(90)">Hiring and staff development</text>
    <text class="category-label" transform="translate(1027,1142) rotate(90)">Rent, Utilities and Cleaning</text>
    <text class="category-label" transform="translate(1091,1142) rotate(90)">Special Events</text>
    <text class="category-label" transform="translate(1147,1142) rotate(90)">Total revenue</text>
    <text class="category-label" transform="translate(1214,1142) rotate(90)">Payroll taxes</text>
    <text class="category-label" transform="translate(1272,1142) rotate(90)">Special events and expenses</text>
    <text class="category-label" transform="translate(1335,1142) rotate(90)">Community awareness</text>
    <text class="category-label" transform="translate(1393,1142) rotate(90)">Travel and Meetings</text>
    <text class="category-label" transform="translate(1456,1142) rotate(90)">Travel and Meetings</text>
    <text class="category-label" transform="translate(1515,1142) rotate(90)">supplies and equipment</text>
    <text class="category-label" transform="translate(1576,1142) rotate(90)">Postage, Printings, and Copuing</text>
    <text class="category-label" transform="translate(1630,1142) rotate(90)">Postage, Printings, and Copuing</text>
    <text class="category-label" transform="translate(1698,1142) rotate(90)">Audit and tax fillingfees</text>
    <text class="category-label" transform="translate(1758,1142) rotate(90)">Information Technology</text>
    <text class="category-label" transform="translate(1812,1142) rotate(90)">Business Insurance</text>
    <text class="category-label" transform="translate(1879,1142) rotate(90)">Affilication fees</text>
    <text class="category-label" transform="translate(1941,1142) rotate(90)">Payroll, Online donation and other expenses</text>
    <text class="category-label" transform="translate(2003,1142) rotate(90)">Total Expenses</text>
  </g>
</svg>
</body>
</html>
```